Stationery Set for new venture capital firm

We need a new set of stationery including letterhead, business cards, envelopes, with compliment slips for our new startup venture capital firm known as Halvora.
We make alternative investments globally and hope to have a worldwide network of offices later.

The stationery should be elegant and not too fussy with the use of too many colors.

Venture Capital

```html
<!DOCTYPE html>
<html lang="en">
<head>
<meta charset="utf-8">
<title>Halvora Stationery Set</title>
<link href="https://fonts.googleapis.com/css2?family=Ubuntu:wght@400;500;700&family=Open+Sans:wght@400;600;700&display=swap" rel="stylesheet">
<style>
:root{
  --blue:#0f9de0;
  --grey:#7b7b7b;
  --ink:#3a3a3a;
  --paper:#ffffff;
  --backdrop:#dcdad8;
  --rule:#8a8a8a;
  --edge:#c9c7c5;
}
*{margin:0;padding:0;box-sizing:border-box}
html,body{width:1200px;height:1000px;overflow:hidden}
body{background:var(--backdrop);position:relative;font-family:"Open Sans",Arial,sans-serif;color:var(--ink)}
.sheet{position:absolute;background:var(--paper);overflow:hidden}
.wordmark{font-family:"Ubuntu",Arial,sans-serif;font-weight:400;color:var(--grey);line-height:1;position:absolute}
.blue{color:var(--blue);font-weight:700}
.accent-bar{position:absolute;left:0;bottom:0;width:100%;background:var(--blue)}

/* Letterhead */
.letterhead{left:50px;top:72px;width:490px;height:695px}
.letterhead .web{position:absolute;top:80px;width:100%;text-align:center;font-size:8px;font-weight:700;color:var(--blue)}
.letterhead .wordmark{left:32px;top:653px;font-size:24px}
.letterhead .footer{position:absolute;left:121px;top:662px;font-size:8.4px;white-space:nowrap}

/* Compliment slip */
.slip{left:581px;top:72px;width:421px;height:234px}
.slip .title{position:absolute;left:22px;top:29px;font-size:8.5px;color:#555}
.slip .lines{position:absolute;left:22px;top:46px;width:372px}
.slip .lines span{display:block;height:14.8px;border-bottom:1px dotted var(--rule)}
.slip .contact{position:absolute;left:23px;top:178px;font-size:7.5px;line-height:11px}
.slip .wordmark{right:27px;top:207px;font-size:14px}

/* Envelopes */
.envelope-back{left:636px;top:500px;width:529px;height:270px}
.envelope{left:579px;top:413px;width:529px;height:274px;box-shadow:2px 3px 0 var(--edge)}
.envelope .wordmark{left:28px;top:97px;font-size:24px}
.envelope .contact{position:absolute;left:28px;top:158px;font-size:7.5px;line-height:11px}
.envelope .accent-bar{height:10px}

/* Business cards */
.card{width:207px;height:118px;top:831px;border-radius:2px}
.card-front{left:50px}
.card-front .wordmark{left:13px;top:78px;font-size:24px}
.card-front .person{position:absolute;right:17px;top:51px;text-align:right;font-size:8px;line-height:11px;color:var(--blue);font-weight:600}
.card-front .accent-bar{height:6px}
.card-back{left:290px;top:830px;width:210px;height:119px;background:var(--blue)}
.card-back .contact{position:absolute;right:16px;top:57px;text-align:right;font-size:6.8px;line-height:9.6px;color:#fff}
</style>
</head>
<body>

<section class="sheet letterhead" aria-label="Letterhead">
  <p class="web">www.halvora.com</p>
  <p class="wordmark">Halvora</p>
  <p class="footer">14 Marlow Court Road, London, E2 7QT <span class="blue">T:</span> 020 7946 0321 <span class="blue">email:</span> info@halvora.com</p>
</section>

<section class="sheet slip" aria-label="Compliment slip">
  <p class="title">With Compliment</p>
  <div class="lines"><span></span><span></span><span></span><span></span><span></span><span></span><span></span><span></span></div>
  <p class="contact">14 Marlow Court Road, London<br>E2 7QT <span class="blue">T:</span> 020 7946 0321<br><span class="blue">email:</span> info@halvora.com<br><span class="blue">www.halvora.com</span></p>
  <p class="wordmark">Halvora</p>
</section>

<section class="sheet envelope-back" aria-label="Envelope back"></section>

<section class="sheet envelope" aria-label="Envelope">
  <p class="wordmark">Halvora</p>
  <p class="contact">14 Marlow Court Road<br>London, E2 7QT<br><span class="blue">T:</span> 020 7946 0321<br><span class="blue">email:</span> info@halvora.com<br><span class="blue">www.halvora.com</span></p>
  <div class="accent-bar"></div>
</section>

<section class="sheet card card-front" aria-label="Business card front">
  <p class="wordmark">Halvora</p>
  <p class="person">Elena Marsh<br>General Manager</p>
  <div class="accent-bar"></div>
</section>

<section class="sheet card card-back" aria-label="Business card back">
  <p class="contact">14 Marlow Court Road<br>London, E2 7QT<br>T: 020 7946 0321<br>email: info@halvora.com<br>www.halvora.com</p>
</section>

</body>
</html>
```